Computer consultant business card

Plimvo Software is a newly started computer consulting company. It's a small one-man company that provides mostly Android applications but also websites in collaboration with designers. I'm running this company on the side of full time university studies.

I want the final design to be clean and memorable. Be creative! :)

Some inspiration:
http://www.artfenwick.com/design/62242
http://www.artfenwick.com/design/1628455/business-card-design-by-brusqlin
http://www.artfenwick.com/design/918507/business-card-design-by-velinora-quathbridge

See attachment for my company logo.
Updates

I would like to thank everyone for submitting! I'll need a couple of days to review and ultimately select a design.

Target Market(s)

Non-technical entrepreneurs and small companies.

Industry/Entity Type

University

Requirements
Must have
• My company logo.
In any way, both colors from my logo.
First- and last name, e-mail and phone number.
Double-sided design.
Nice to have
• Something creative with the symbol in my logo

```html
<!DOCTYPE html>
<html lang="en">
<head>
<meta charset="utf-8">
<title>Plimvo Software – Business Card</title>
<link rel="stylesheet" href="https://fonts.googleapis.com/css2?family=Arimo:wght@400;700&display=swap">
<style>
  :root {
    --page-bg: #2b2b2d;
    --card-white: #ffffff;
    --ink-dark: #2e2e30;
    --brand-blue: #1e7ff5;
    --brand-cyan: #1fd0f5;
    --brand-deep: #2273f0;
  }
  * { margin: 0; padding: 0; box-sizing: border-box; }
  html, body {
    width: 1200px;
    height: 1001px;
    overflow: hidden;
    background: var(--page-bg);
    font-family: "Arimo", Arial, sans-serif;
  }
  .card {
    position: absolute;
    left: 250px;
    width: 700px;
    height: 400px;
    box-shadow: 0 10px 30px rgba(0,0,0,0.45);
  }
  .card-front { top: 70px; background: var(--card-white); }
  .card-back {
    top: 530px;
    background: radial-gradient(ellipse at 45% 50%, var(--brand-cyan) 0%, #1fa8f5 35%, var(--brand-deep) 80%);
  }
  .person {
    position: absolute;
    top: 34px;
    right: 40px;
    text-align: right;
    line-height: 1.05;
  }
  .person-first { color: var(--brand-blue); font-weight: 700; font-size: 24px; }
  .person-last { color: var(--ink-dark); font-size: 18px; }
  .contact {
    position: absolute;
    right: 40px;
    bottom: 120px;
    text-align: right;
    color: var(--ink-dark);
    font-size: 19px;
    line-height: 1.35;
  }
  .contact-label { color: var(--brand-blue); font-weight: 700; }
  .brand {
    position: absolute;
    display: flex;
    align-items: center;
  }
  .brand-dot { border-radius: 50%; flex: none; }
  .brand-name { font-weight: 400; letter-spacing: 1px; }
  .card-front .brand { left: 40px; bottom: 40px; gap: 18px; }
  .card-front .brand-dot { width: 80px; height: 80px; background: var(--brand-blue); }
  .card-front .brand-name { color: var(--ink-dark); font-size: 64px; }
  .card-back .brand { left: 50%; top: 50%; transform: translate(-50%, -50%); gap: 28px; }
  .card-back .brand-dot { width: 130px; height: 130px; background: var(--card-white); }
  .card-back .brand-name { color: var(--card-white); font-size: 104px; }
</style>
</head>
<body>
  <section class="card card-front">
    <div class="person">
      <div class="person-first">First Name</div>
      <div class="person-last">Last Name</div>
    </div>
    <div class="contact">
      <div>Street Name, City Name</div>
      <div>State, City Zip Code</div>
      <div><span class="contact-label">P :</span> 123-456-7321 <span class="contact-label">E :</span> info@plimvo.com</div>
    </div>
    <div class="brand">
      <span class="brand-dot"></span>
      <span class="brand-name">Plimvo</span>
    </div>
  </section>

  <section class="card card-back">
    <div class="brand">
      <span class="brand-dot"></span>
      <span class="brand-name">Plimvo</span>
    </div>
  </section>
</body>
</html>
```